Party Sticker Designs for Kids Parties

I need 13 Sticker Designs for 13 different kid parties. Also, several stickers with have multiple versions: same design, but different texts. All versions will need to have both a 3x3 round and 3x3 square design. I’ve provided a lot of examples and stock designs. My design notes (summer2020_DesignGraphic_Notes) include the look I like best on the left and some other ideas on the right – the main goal is a good design. We will need all stickers in jpg, eps, png, psd, and ai formats.

```html
<!DOCTYPE html>
<html lang="en">
<head>
<meta charset="utf-8">
<title>Kids Party Sticker Sheet</title>
<link rel="stylesheet" href="https://fonts.googleapis.com/css2?family=Archivo+Black&family=Lora:ital,wght@1,700&family=Roboto+Slab:wght@400;700;800&display=swap">
<style>
  :root {
    --sheet-bg: #ffffff;
    --plaid-pink: #f3a8e2;
    --troop-green: #4cc72b;
    --troop-teal: #7fdcdc;
    --troop-pink: #e8449a;
    --chevron-mint: #91e8df;
    --band-grey: #8c8c8c;
    --band-line: #6f6f6f;
    --ink: #141414;
    --gingham-red: #ef6d6d;
    --bbq-red: #e1232b;
    --white: #ffffff;
  }
  html, body {
    margin: 0;
    padding: 0;
    width: 1200px;
    height: 1200px;
    overflow: hidden;
    background: var(--sheet-bg);
  }
  .sticker-sheet { display: block; width: 1200px; height: 1200px; }
  .troop-arc { font-family: "Archivo Black", sans-serif; font-size: 12px; fill: var(--white); letter-spacing: 0.4px; }
  .troop-arc--bottom { font-size: 11.5px; }
  .troop-name { font-family: "Archivo Black", sans-serif; font-size: 6px; fill: var(--troop-pink); }
  .party-headline { font-family: "Archivo Black", sans-serif; font-size: 11px; fill: var(--ink); }
  .party-script { font-family: "Lora", serif; font-style: italic; font-weight: 700; font-size: 12px; fill: var(--ink); }
  .party-little { font-family: "Roboto Slab", serif; font-size: 10px; fill: var(--ink); }
  .party-man { font-family: "Roboto Slab", serif; font-weight: 800; font-size: 10px; fill: var(--ink); }
  .bbq-title { font-family: "Roboto Slab", serif; font-weight: 800; font-size: 13px; fill: var(--bbq-red); }
  .bbq-title--wide { font-size: 12px; }
</style>
</head>
<body>
<svg class="sticker-sheet" viewBox="0 0 1200 1200" xmlns="http://www.w3.org/2000/svg">
  <defs>
    <clipPath id="round-clip"><circle cx="70" cy="70" r="70"/></clipPath>
    <path id="troop-arc-top" d="M 23,70 A 47,47 0 0 1 117,70"/>
    <path id="troop-arc-bottom" d="M 15,70 A 55,55 0 0 0 125,70"/>

    <g id="troop-backdrop">
      <rect width="140" height="140" fill="var(--plaid-pink)" role="img" aria-label="Pink and white plaid pattern"/>
      <rect y="31" width="140" height="9" fill="var(--troop-green)"/>
      <rect y="43" width="140" height="3" fill="var(--troop-green)"/>
      <rect y="94" width="140" height="3" fill="var(--troop-green)"/>
      <rect y="100" width="140" height="9" fill="var(--troop-green)"/>
    </g>
    <g id="troop-emblem">
      <circle cx="70" cy="70" r="58" fill="var(--troop-green)"/>
      <circle cx="70" cy="70" r="44" fill="var(--white)"/>
      <circle cx="70" cy="70" r="38" fill="var(--troop-teal)" stroke="var(--troop-pink)" stroke-width="2"/>
      <circle cx="18" cy="70" r="2.2" fill="var(--white)"/>
      <circle cx="122" cy="70" r="2.2" fill="var(--white)"/>
      <text class="troop-name" x="70" y="68" text-anchor="middle">MEADOWLARK</text>
      <text class="troop-name" x="70" y="77" text-anchor="middle">GIRLS CLUB</text>
    </g>

    <g id="chevron-backdrop">
      <rect width="140" height="140" fill="var(--chevron-mint)" role="img" aria-label="Mint and white chevron pattern"/>
      <rect y="55" width="140" height="30" fill="var(--band-grey)"/>
      <rect y="58" width="140" height="1" fill="var(--band-line)"/>
      <rect y="81" width="140" height="1" fill="var(--band-line)"/>
    </g>
    <g id="chevron-medallion">
      <circle cx="70" cy="70" r="45" fill="var(--white)" stroke="#a0a0a0" stroke-width="1.5"/>
      <circle cx="70" cy="70" r="41" fill="none" stroke="var(--ink)" stroke-width="1" stroke-dasharray="1 2"/>
    </g>

    <g id="gingham-backdrop">
      <rect width="140" height="140" fill="var(--gingham-red)" role="img" aria-label="Red and white gingham pattern"/>
    </g>
    <g id="bbq-medallion">
      <circle cx="70" cy="70" r="53" fill="var(--white)" stroke="var(--bbq-red)" stroke-width="2.5"/>
      <rect x="48" y="26" width="44" height="30" rx="5" fill="#2c2c2c" role="img" aria-label="Crossed grill fork and spatula"/>
      <line x1="26" y1="60" x2="114" y2="60" stroke="var(--ink)" stroke-width="1.5"/>
      <line x1="26" y1="82" x2="114" y2="82" stroke="var(--ink)" stroke-width="1.5"/>
      <circle cx="70" cy="94" r="4.5" fill="#2c2c2c" role="img" aria-label="Small grill flame"/>
    </g>
  </defs>

  <!-- Row 1: troop birthday / baby girl -->
  <g class="sticker sticker--square troop-sticker" transform="translate(127.5 105) scale(1.5)">
    <use href="#troop-backdrop"/><use href="#troop-emblem"/>
    <text class="troop-arc"><textPath href="#troop-arc-top" startOffset="50%" text-anchor="middle">TROOP 332</textPath></text>
    <text class="troop-arc troop-arc--bottom"><textPath href="#troop-arc-bottom" startOffset="50%" text-anchor="middle">BIRTHDAY GIRL</textPath></text>
  </g>
  <g class="sticker sticker--round troop-sticker" transform="translate(375 105) scale(1.5)">
    <g clip-path="url(#round-clip)"><use href="#troop-backdrop"/></g><use href="#troop-emblem"/>
    <text class="troop-arc"><textPath href="#troop-arc-top" startOffset="50%" text-anchor="middle">TROOP 332</textPath></text>
    <text class="troop-arc troop-arc--bottom"><textPath href="#troop-arc-bottom" startOffset="50%" text-anchor="middle">BIRTHDAY GIRL</textPath></text>
  </g>
  <g class="sticker sticker--square troop-sticker" transform="translate(630 105) scale(1.5)">
    <use href="#troop-backdrop"/><use href="#troop-emblem"/>
    <text class="troop-arc"><textPath href="#troop-arc-top" startOffset="50%" text-anchor="middle">TROOP 332</textPath></text>
    <text class="troop-arc troop-arc--bottom"><textPath href="#troop-arc-bottom" startOffset="50%" text-anchor="middle">BABY GIRL</textPath></text>
  </g>
  <g class="sticker sticker--round troop-sticker" transform="translate(870 105) scale(1.5)">
    <g clip-path="url(#round-clip)"><use href="#troop-backdrop"/></g><use href="#troop-emblem"/>
    <text class="troop-arc"><textPath href="#troop-arc-top" startOffset="50%" text-anchor="middle">TROOP 332</textPath></text>
    <text class="troop-arc troop-arc--bottom"><textPath href="#troop-arc-bottom" startOffset="50%" text-anchor="middle">BABY GIRL</textPath></text>
  </g>

  <!-- Row 2: little man -->
  <g class="sticker sticker--square little-man-sticker" transform="translate(127.5 345) scale(1.5)">
    <use href="#chevron-backdrop"/><use href="#chevron-medallion"/>
    <text class="party-headline" x="70" y="46" text-anchor="middle">HAPPY</text>
    <text class="party-script" x="70" y="59" text-anchor="middle">Birthday</text>
    <rect x="57" y="63" width="26" height="13" rx="3" fill="var(--ink)" role="img" aria-label="Black bow tie"/>
    <text class="party-little" x="70" y="88" text-anchor="middle">Little</text>
    <text class="party-man" x="70" y="100" text-anchor="middle">MAN</text>
  </g>
  <g class="sticker sticker--round little-man-sticker" transform="translate(375 345) scale(1.5)">
    <g clip-path="url(#round-clip)"><use href="#chevron-backdrop"/></g><use href="#chevron-medallion"/>
    <text class="party-headline" x="70" y="46" text-anchor="middle">HAPPY</text>
    <text class="party-script" x="70" y="59" text-anchor="middle">Birthday</text>
    <rect x="57" y="63" width="26" height="13" rx="3" fill="var(--ink)" role="img" aria-label="Black bow tie"/>
    <text class="party-little" x="70" y="88" text-anchor="middle">Little</text>
    <text class="party-man" x="70" y="100" text-anchor="middle">MAN</text>
  </g>
  <g class="sticker sticker--square little-man-sticker" transform="translate(630 345) scale(1.5)">
    <use href="#chevron-backdrop"/><use href="#chevron-medallion"/>
    <text class="party-headline" x="70" y="52" text-anchor="middle">WELCOME</text>
    <rect x="57" y="57" width="26" height="13" rx="3" fill="var(--ink)" role="img" aria-label="Black bow tie"/>
    <text class="party-little" x="70" y="84" text-anchor="middle">Little</text>
    <text class="party-man" x="70" y="96" text-anchor="middle">MAN</text>
  </g>
  <g class="sticker sticker--round little-man-sticker" transform="translate(870 345) scale(1.5)">
    <g clip-path="url(#round-clip)"><use href="#chevron-backdrop"/></g><use href="#chevron-medallion"/>
    <text class="party-headline" x="70" y="52" text-anchor="middle">WELCOME</text>
    <rect x="57" y="57" width="26" height="13" rx="3" fill="var(--ink)" role="img" aria-label="Black bow tie"/>
    <text class="party-little" x="70" y="84" text-anchor="middle">Little</text>
    <text class="party-man" x="70" y="96" text-anchor="middle">MAN</text>
  </g>

  <!-- Row 3: I Do BBQ / BaBy Q -->
  <g class="sticker sticker--square bbq-sticker" transform="translate(127.5 597) scale(1.5)">
    <use href="#gingham-backdrop"/><use href="#bbq-medallion"/>
    <text class="bbq-title" x="70" y="76" text-anchor="middle">I Do BBQ</text>
  </g>
  <g class="sticker sticker--round bbq-sticker" transform="translate(375 597) scale(1.5)">
    <g clip-path="url(#round-clip)"><use href="#gingham-backdrop"/></g><use href="#bbq-medallion"/>
    <text class="bbq-title" x="70" y="76" text-anchor="middle">I Do BBQ</text>
  </g>
  <g class="sticker sticker--square bbq-sticker" transform="translate(630 597) scale(1.5)">
    <use href="#gingham-backdrop"/><use href="#bbq-medallion"/>
    <text class="bbq-title" x="70" y="76" text-anchor="middle">BaBy Q</text>
  </g>
  <g class="sticker sticker--round bbq-sticker" transform="translate(870 597) scale(1.5)">
    <g clip-path="url(#round-clip)"><use href="#gingham-backdrop"/></g><use href="#bbq-medallion"/>
    <text class="bbq-title" x="70" y="76" text-anchor="middle">BaBy Q</text>
  </g>

  <!-- Row 4: Bday BQ / BBQ -->
  <g class="sticker sticker--square bbq-sticker" transform="translate(127.5 837) scale(1.5)">
    <use href="#gingham-backdrop"/><use href="#bbq-medallion"/>
    <text class="bbq-title bbq-title--wide" x="70" y="76" text-anchor="middle">Bday BQ</text>
  </g>
  <g class="sticker sticker--round bbq-sticker" transform="translate(375 837) scale(1.5)">
    <g clip-path="url(#round-clip)"><use href="#gingham-backdrop"/></g><use href="#bbq-medallion"/>
    <text class="bbq-title bbq-title--wide" x="70" y="76" text-anchor="middle">Bday BQ</text>
  </g>
  <g class="sticker sticker--square bbq-sticker" transform="translate(630 837) scale(1.5)">
    <use href="#gingham-backdrop"/><use href="#bbq-medallion"/>
    <text class="bbq-title" x="70" y="76" text-anchor="middle">BBQ</text>
  </g>
  <g class="sticker sticker--round bbq-sticker" transform="translate(870 837) scale(1.5)">
    <g clip-path="url(#round-clip)"><use href="#gingham-backdrop"/></g><use href="#bbq-medallion"/>
    <text class="bbq-title" x="70" y="76" text-anchor="middle">BBQ</text>
  </g>
</svg>
</body>
</html>
```